Website Design for a Project Management Consulting Business

I have a logo design already and now I need a website.
I am a project manager and run my own consulting business.
Currently I am under contract with 3 major Kestrelmark 300 companies. I'd like a website I can direct current and future clients.
My job is running IT projects and working with developers to deliver business priorities.
The website should be professional and clean - I work IT projects and would like to incorporate that into any theme.
I'd like the site to have several page or breakoff links - sections would include : about me, about my services, a page to display all of my certification badges, another page to talk about highlights from past projects and so on.
Looking for a collaborative experience.

Industry/Entity Type

Kestrelmark 300 Consulting Firm - Project Management

Coding

Coded - Design and coding required

Number of Pages Required

1 page

Font styles to use
Serif

Colors
0094D4
00A9DD
6FCCEA
C7EBF8
E9F6FB
EE7325
F08F49
F5BC92
FAE3D3
FDF4ED

Requirements
Must have
• Sections that are a must: About Me (bio), About My Services, About my Certifications and Credentials, Experience on Past Projects,
Nice to have
• I have added the logo below - I'd like to use the logo and have it prominent ; should be professional and inviting

```html
<!DOCTYPE html>
<html lang="en">
<head>
<meta charset="utf-8">
<title>Meridian Project Management Consulting</title>
<link href="https://fonts.googleapis.com/css2?family=Michroma&family=Barlow:wght@400;500;600;700&display=swap" rel="stylesheet">
<style>
:root{
  --navy:#0b1f4a;
  --navy-deep:#06143a;
  --blue:#0a7fd6;
  --blue-bright:#0094d4;
  --sky:#6fcceA;
  --pale:#e9f6fb;
  --grey-bg:#eef1f5;
  --ink:#1d2433;
  --muted:#5b6577;
  --white:#ffffff;
  --head:"Michroma", sans-serif;
  --body:"Barlow", sans-serif;
}
*{box-sizing:border-box;margin:0;padding:0}
html,body{width:1200px;height:4152px;overflow:hidden}
body{position:relative;background:var(--white);font-family:var(--body);color:var(--ink)}
.abs{position:absolute}
.btn{position:absolute;display:inline-block;background:var(--blue-bright);color:var(--white);font:600 15px var(--body);letter-spacing:1.5px;padding:13px 30px;border-radius:22px}
.btn.outline{background:transparent;border:2px solid var(--white)}
.ghost{position:absolute;font-family:var(--head);font-size:64px;letter-spacing:4px;white-space:nowrap}
.heading{position:absolute;font-family:var(--head);font-size:38px;letter-spacing:3px;color:var(--ink);white-space:nowrap}

/* nav */
.site-nav{position:absolute;top:0;left:0;width:1200px;height:72px;background:var(--white);z-index:5}
.brand{position:absolute;left:40px;top:18px;display:flex;align-items:center;gap:10px}
.brand-square{width:34px;height:34px;background:var(--blue-bright)}
.brand-name{font:700 26px var(--body);color:var(--navy);letter-spacing:2px}
.nav-links{position:absolute;right:60px;top:28px;display:flex;gap:60px;font:500 15px var(--body);letter-spacing:1.5px;color:var(--navy)}
.nav-links .active{border-bottom:2px solid var(--blue-bright);padding-bottom:4px}

/* hero */
.hero{position:absolute;top:72px;left:0;width:1200px;height:660px;background:radial-gradient(ellipse at 30% 70%,#1a6fd0 0%,#0c2c78 35%,var(--navy-deep) 75%)}
.hero-photo{position:absolute;left:720px;top:0;width:300px;height:600px;background:linear-gradient(180deg,#4a5a78,#283552);border-radius:4px 4px 0 0}
.hero-kicker{position:absolute;left:100px;top:195px;color:var(--white);font:500 17px var(--head);letter-spacing:3px}
.hero-title{position:absolute;left:100px;top:230px;color:var(--white);font:400 46px/54px var(--head);letter-spacing:2px}

/* about */
.about-title{left:590px;top:852px}
.about-text{position:absolute;left:590px;width:500px;font:400 17px/27px var(--body);color:var(--muted)}

/* services */
.services-title{left:0;width:1200px;text-align:center;top:1492px;color:var(--white)}
.service{position:absolute;width:260px;color:var(--white)}
.service h3{font:700 15px var(--body);letter-spacing:1px;margin-bottom:6px}
.service p{font:400 13px/19px var(--body);color:#d7ecfb}
.service.left{text-align:right}

/* certificates */
.certs{position:absolute;top:2040px;left:0;width:1200px;height:450px;background:var(--grey-bg)}
.cert-group{position:absolute;top:2270px;width:300px;text-align:center}
.cert-group .badges{display:flex;justify-content:center;gap:14px;margin-bottom:16px}
.cert-group .org{font:500 15px var(--body);color:var(--blue-bright)}
.cert-group .name{font:500 19px var(--body);color:var(--ink)}

/* projects */
.project{position:absolute;top:2830px;height:300px}
.project .shot{position:absolute;inset:0}
.project .cap{position:absolute;left:0;right:0;bottom:28px;text-align:center;color:var(--white)}
.project .cap b{display:block;font:700 17px var(--body);letter-spacing:.5px}
.project .cap span{font:400 13px var(--body);color:#d6e2f2}

/* contact */
.field{position:absolute;left:628px;width:420px;border-bottom:1px solid #8fa2c8;color:var(--white);font:400 16px var(--body);padding-bottom:10px}

/* footer */
.foot-col{position:absolute;top:3880px}
.foot-col h4{font:500 16px var(--head);letter-spacing:2px;color:var(--navy);padding-bottom:10px;border-bottom:2px solid var(--blue-bright);margin-bottom:16px;width:200px}
.foot-col li{list-style:none;font:400 15px/27px var(--body);color:var(--ink)}
.contact-line{display:flex;align-items:flex-start;gap:12px;font:400 14px/20px var(--body);margin-bottom:18px;color:var(--ink)}
.dot{width:26px;height:26px;border-radius:50%;background:var(--blue-bright);flex:none;display:flex;align-items:center;justify-content:center}
</style>
</head>
<body>

<nav class="site-nav">
  <div class="brand"><span class="brand-square"></span><span class="brand-name">MERIDIAN</span></div>
  <div class="nav-links"><span class="active">ABOUT ME</span><span>SERVICES</span><span>PROJECTS</span><span>CERTIFICATES</span><span>CONTACT</span></div>
</nav>

<header class="hero">
  <div class="abs" role="img" aria-label="Glowing digital particle wave across dark blue background" style="left:0;top:380px;width:1200px;height:200px;background:radial-gradient(ellipse at 60% 50%,rgba(111,204,234,.35),transparent 65%)"></div>
  <div class="hero-photo" role="img" aria-label="Portrait of the consultant in a grey suit and tie"></div>
  <div class="hero-kicker">WELCOME TO MERIDIAN</div>
  <h1 class="hero-title">PROJECT<br>MANAGEMENT<br>CONSULTING</h1>
  <span class="btn" style="left:100px;top:430px">LEARN MORE</span>
</header>
<svg class="abs" style="left:0;top:560px" width="1200" height="180" viewBox="0 0 1200 180">
  <polygon points="0,160 1200,40 1200,180 0,180" fill="#ffffff"/>
  <polygon points="700,130 1200,40 1200,90 1000,110" fill="#0094d4"/>
  <polygon points="0,150 420,125 0,175" fill="#0a7fd6"/>
</svg>

<!-- about -->
<section>
  <svg class="abs" style="left:96px;top:800px" width="340" height="400" viewBox="0 0 340 400">
    <polygon points="170,4 336,100 336,300 170,396 4,300 4,100" fill="none" stroke="#0094d4" stroke-width="3"/>
  </svg>
  <div class="abs" role="img" aria-label="Smiling portrait of the consultant" style="left:112px;top:820px;width:308px;height:360px;clip-path:polygon(50% 0,100% 25%,100% 75%,50% 100%,0 75%,0 25%);background:linear-gradient(160deg,#5a4a44,#1c1d24)"></div>
  <div class="ghost" style="left:700px;top:810px;color:#f0f2f5">ABOUT</div>
  <h2 class="heading about-title">ABOUT ME</h2>
  <p class="about-text" style="top:905px">Lorem ipsum dolor sit amet, consectetur adipiscing elit, sed do eiusmod tempor incididunt ut labore et dolore magna aliqua. Ut enim ad minim veniam, quis nostrud exercitation ullamco laboris nisi ut aliquip ex ea commodo consequat.</p>
  <p class="about-text" style="top:1035px">Duis aute irure dolor in reprehenderit in voluptate velit esse cillum dolore eu fugiat nulla pariatur. Excepteur sint occaecat cupidatat non proident, sunt in culpa qui officia deserunt mollit anim id est laborum.</p>
  <span class="btn" style="left:590px;top:1150px">LEARN MORE</span>
</section>

<!-- services -->
<section>
  <svg class="abs" style="left:0;top:1330px" width="1200" height="700" viewBox="0 0 1200 700">
    <polygon points="0,90 1200,0 1200,40 0,130" fill="#0b1f4a"/>
    <polygon points="0,130 1200,40 1200,610 0,660" fill="#0a86e0"/>
    <polygon points="0,660 1200,610 1200,650 0,700" fill="#0b1f4a"/>
    <g stroke="#bfe3fb" stroke-width="2" fill="none">
      <path d="M420,378 H470 V420 H500"/><path d="M420,460 H470 V420"/>
      <path d="M780,378 H730 V420 H700"/><path d="M780,460 H730 V420"/>
    </g>
    <rect x="500" y="330" width="200" height="180" fill="#ffffff"/>
    <rect x="516" y="346" width="168" height="148" fill="none" stroke="#0b1f4a" stroke-width="4"/>
    <text x="600" y="428" text-anchor="middle" font-family="Barlow, sans-serif" font-weight="700" font-size="22" fill="#0b1f4a">MERIDIAN</text>
    <g fill="#ffffff"><circle cx="420" cy="378" r="28"/><circle cx="420" cy="478" r="28"/><circle cx="780" cy="378" r="28"/><circle cx="780" cy="478" r="28"/></g>
    <g stroke="#0a86e0" stroke-width="3" fill="none">
      <path d="M408,378 l8,8 l14,-16"/><rect x="408" y="468" width="24" height="18"/>
      <path d="M768,388 h24 M772,378 h16 M776,368 h8"/><circle cx="780" cy="472" r="8"/><path d="M766,492 q14,-14 28,0"/>
    </g>
  </svg>
  <div class="ghost" style="left:0;width:1200px;text-align:center;top:1472px;color:rgba(255,255,255,.12)">SERVICES</div>
  <h2 class="heading services-title">MY SERVICES</h2>
  <div class="service left" style="left:120px;top:1620px"><h3>CONSULTING SERVICE</h3><p>Lorem ipsum dolor sit amet, conse ctetur adipiscing elit, sed do eiusmod tempor incididunt.</p></div>
  <div class="service left" style="left:120px;top:1778px"><h3>PROJECT MANAGEMENT</h3><p>Lorem ipsum dolor sit amet, conse ctetur adipiscing elit, sed do eiusmod tempor incididunt.</p></div>
  <div class="service" style="left:830px;top:1620px"><h3>LOREM IPSUM SERVICE</h3><p>Lorem ipsum dolor sit amet, conse ctetur adipiscing elit, sed do eiusmod tempor incididunt.</p></div>
  <div class="service" style="left:830px;top:1778px"><h3>TRAINING SERVICE</h3><p>Lorem ipsum dolor sit amet, conse ctetur adipiscing elit, sed do eiusmod tempor incididunt.</p></div>
  <span class="btn outline" style="left:515px;top:1880px">LEARN MORE</span>
</section>

<!-- certificates -->
<section class="certs"></section>
<div class="ghost" style="left:80px;top:2080px;color:#e1e5eb">CERTIFICATE</div>
<div class="abs" style="left:80px;top:2122px;font:500 14px var(--head);letter-spacing:2px;color:var(--blue-bright)">MY CERTIFICATE</div>
<h2 class="heading" style="left:80px;top:2140px">CERTIFICATES</h2>
<div class="cert-group" style="left:150px">
  <div class="badges"><svg width="90" height="90"><circle cx="45" cy="45" r="42" fill="#4b2a8a"/></svg><svg width="90" height="90"><circle cx="45" cy="45" r="42" fill="#5a3aa0"/></svg></div>
  <div class="org">Organization</div><div class="name">Project Leadership Guild</div>
</div>
<div class="cert-group" style="left:450px">
  <div class="badges"><svg width="90" height="90"><polygon points="45,3 85,25 85,65 45,87 5,65 5,25" fill="#f0b429"/></svg><svg width="90" height="90"><polygon points="45,3 85,25 85,65 45,87 5,65 5,25" fill="#ee7325"/></svg></div>
  <div class="org">Organization</div><div class="name">Agile Practice Council</div>
</div>
<div class="cert-group" style="left:750px">
  <div class="badges"><svg width="90" height="90"><polygon points="45,3 85,25 85,65 45,87 5,65 5,25" fill="#1e2a52"/></svg><svg width="90" height="90"><polygon points="45,3 85,25 85,65 45,87 5,65 5,25" fill="#2a3a66"/></svg></div>
  <div class="org">Organization</div><div class="name">Scaled Delivery Network</div>
</div>

<!-- projects -->
<section>
  <div class="ghost" style="left:0;width:1200px;text-align:center;top:2650px;color:#f0f2f5">PROJECTS</div>
  <h2 class="heading" style="left:0;width:1200px;text-align:center;top:2695px">LATEST PROJECTS</h2>
  <div class="project" style="left:0;width:280px"><div class="shot" role="img" aria-label="Colleagues meeting at a desk with laptops" style="background:linear-gradient(180deg,#7d8a9c,#1f2c48)"></div><div class="cap"><b>LOREM IPSUM IS SIMPLY</b><span>Lorem Ipsum has been the industry's</span></div></div>
  <div class="project" style="left:290px;width:185px;top:2800px;height:360px;background:var(--blue-bright)">
    <div style="position:absolute;left:18px;right:18px;top:70px;text-align:center;color:#fff">
      <div style="font:700 17px/22px var(--body)">SED UT PERSPICIATIS UNDE OMNIS ISTE</div>
      <p style="font:400 12px/17px var(--body);margin-top:10px;color:#e4f3fc">Lorem ipsum dolor sit amet, consectetur adipiscing elit, sed do eiusmod tempor incididunt ut labore et dolore magna aliqua. Ut enim ad minim veniam.</p>
    </div>
    <svg style="position:absolute;left:72px;top:268px" width="40" height="40"><circle cx="20" cy="20" r="18" fill="none" stroke="#fff" stroke-width="2"/><path d="M13,17 l7,7 l7,-7" stroke="#fff" stroke-width="2" fill="none"/></svg>
  </div>
  <div class="project" style="left:485px;width:240px"><div class="shot" role="img" aria-label="Control room with monitors" style="background:linear-gradient(180deg,#2b5c9c,#0c1d44)"></div><div class="cap"><b>LOREM IPSUM IS SIMPLY</b><span>Lorem Ipsum has been the industry's</span></div></div>
  <div class="project" style="left:735px;width:180px"><div class="shot" role="img" aria-label="Team reviewing data screens" style="background:linear-gradient(180deg,#3a6ab0,#0f2350)"></div><div class="cap"><b>LOREM IPSUM IS SIMPLY</b><span>Lorem Ipsum has been</span></div></div>
  <div class="project" style="left:925px;width:275px"><div class="shot" role="img" aria-label="Two colleagues discussing at a table" style="background:linear-gradient(180deg,#9aa4b2,#2a3550)"></div><div class="cap"><b>LOREM IPSUM IS SIMPLY</b><span>Lorem Ipsum has been the industry's</span></div></div>
</section>

<!-- contact -->
<section>
  <svg class="abs" style="left:0;top:3250px" width="1200" height="580" viewBox="0 0 1200 580">
    <polygon points="0,40 1200,0 1200,580 0,580" fill="#0b1f4a"/>
    <polygon points="0,40 600,20 0,70" fill="#0a86e0"/>
  </svg>
  <div class="abs" role="img" aria-label="Business team photo with large arrow graphic" style="left:140px;top:3340px;width:400px;height:400px;background:linear-gradient(135deg,#6fa8dc,#1e4f99 55%,#0b2660)"></div>
  <div class="ghost" style="left:790px;top:3310px;color:rgba(255,255,255,.08)">CONTACT</div>
  <div class="abs" style="left:628px;top:3325px;font:500 15px var(--head);letter-spacing:3px;color:#cfe1f5">GET IN TOUCH</div>
  <h2 class="heading" style="left:628px;top:3345px;color:#fff">CONTACT ME</h2>
  <div class="field" style="top:3420px">Name</div>
  <div class="field" style="top:3475px">Phone Number</div>
  <div class="field" style="top:3530px">Email Address</div>
  <div class="field" style="top:3585px;height:80px">Message</div>
  <span class="btn" style="left:628px;top:3690px;border-radius:2px;padding:12px 32px">SEND ENQUIRY</span>
</section>

<!-- footer -->
<footer>
  <div class="brand" style="top:3880px;left:120px;position:absolute"><span class="brand-square"></span><span class="brand-name">MERIDIAN</span></div>
  <svg class="abs" style="left:120px;top:3955px" width="150" height="34"><g fill="#0a4fa8"><circle cx="16" cy="17" r="15"/><circle cx="52" cy="17" r="15"/><circle cx="88" cy="17" r="15"/><circle cx="124" cy="17" r="15"/></g></svg>
  <div class="abs" style="left:120px;top:4010px;font:400 14px var(--body);color:var(--muted)">Copyright 2022 Meridian LLC All Right Reserved</div>
  <div class="foot-col" style="left:490px"><h4>NAVIGATION</h4><ul><li>About Me</li><li>Services Provide</li><li>Projects</li><li>Certifications</li></ul></div>
  <div class="foot-col" style="left:680px"><h4>RESOURCES</h4><ul><li>Support</li><li>Privacy Policy</li><li>Contact Us</li></ul></div>
  <div class="foot-col" style="left:870px"><h4>CONTACT US</h4>
    <div class="contact-line"><span class="dot"><svg width="12" height="14"><path d="M6,13 C2,8 1,6 1,5 a5,5 0 0 1 10,0 c0,1 -1,3 -5,8z" fill="#fff"/></svg></span><span>2718 Harbor Crest Lane<br>Suite 40, Lakeview City</span></div>
    <div class="contact-line"><span class="dot"><svg width="12" height="12"><path d="M2,1 l3,0 l1,3 l-2,1 a7,7 0 0 0 3,3 l1,-2 l3,1 l0,3 a10,10 0 0 1 -9,-9z" fill="#fff"/></svg></span><span>(555) 014 2290</span></div>
    <div class="contact-line"><span class="dot"><svg width="12" height="10"><rect x="0.5" y="0.5" width="11" height="9" fill="none" stroke="#fff"/><path d="M1,1 l5,4 l5,-4" stroke="#fff" fill="none"/></svg></span><span>hello@meridianpm.example</span></div>
  </div>
</footer>

</body>
</html>
```